Democracy in crisis book

This book tries to sound the ALARM that we will lose our democracy unless we force Unionists to adopt the plan inside this book. I designed a mock cover (attached) but I am concerned it would not look good in the Thumbnail view that most people would see it as they're scrolling down Shopvale or Pagenook. The final title for the book is: Final Hour to Rescue the Free Republic. The current subtitle is: The Single Path to Halt the 2022 Partisan Takeover & Renew Our Homeland -- but it’s a work in progress.The subtitle is still working progress but it's really not that important and can be small.
STYLE CONSIDERATIONS:
(1) The title should be on 5 separate lines: Final; Hour; To Rescue; Free; Republic
(2) The title could be in white fat letters except for maybe one line that says “To Rescue” which could be in the blue color of the Civic Union Party-- or maybe Free Republic could be in blue. We may have to try a few variations of that.
(3) I picked the red in the mock cover to connotate an emergency,
(4) I liked big bold fat font going across the full page so that it looks like a major warning sign, though note I was unable to extend each line flush all the way to the right which I think would have been better.
(5) I liked it better flush to left instead of centered.
(6) I picked the Harwick monument + a crowd for my mock cover, but a picture of a huge crowd protesting with a picture of the United States Congress in the background would be much better. DO NOT USE HARWICK. Obviously I would need it to be an open license or something I can pay a small amount to get. If you can find that picture then the page should probably be colored in red with Congress in white.
I got the idea 4 giant title from the book “seldom a quiet so bright” and Dellowby’s “When Freedom Fades” or “Grey Herons” by Mara Vostell though I hate that font)
I love Osric Thale’s “marked since the outset” cover so if you find a picture of Congress and a protest crowd instead of painting it red you could have just a couple of jagged red stripes going across it like that cover.
I love the 3-D effect of Greta Wolven's cover for The Silverwren where it looks like a page is being ripped. That effect could be done the words Free Republic like it's being torn off the page UPDATE: MANY DESIGNERS TRIED THAT & IT DID NOT WORK AT ALL.
Note that this book will be submitted to many award competitions, so please give me an award-winning cover.
I like how the title of the book The Unchosen by Martin Fellowes has the words starting to fade. I don't like the ladder on it, but maybe 'Free Republic' could fade like that.
Unionists

```html
<!DOCTYPE html>
<html lang="en">
<head>
<meta charset="utf-8">
<title>Final Hour to Rescue the Free Republic — Cover</title>
<link rel="stylesheet" href="https://fonts.googleapis.com/css2?family=Roboto:wght@400;500;900&display=swap">
<style>
  :root {
    --page-bg: #efefea;
    --alarm-red: #b50f14;
    --deep-red: #6e0a0c;
    --night: #0b0b0c;
    --smoke: #2c2d2f;
    --stone: #6f7174;
    --union-blue: #3b8fe0;
    --rule-red: #c2161c;
    --paper: #ffffff;
  }
  html, body {
    margin: 0;
    padding: 0;
    width: 1200px;
    height: 900px;
    overflow: hidden;
    background: var(--page-bg);
  }
  .book-cover {
    position: absolute;
    left: 362px;
    top: 80px;
    width: 475px;
    height: 735px;
    overflow: hidden;
    background: var(--night);
  }
  .book-cover svg {
    display: block;
    width: 475px;
    height: 735px;
  }
  .title-line {
    font-family: "Roboto", Arial, sans-serif;
    font-weight: 900;
    fill: var(--paper);
  }
  .title-line--accent {
    fill: var(--union-blue);
  }
  .subtitle {
    font-family: "Roboto", Arial, sans-serif;
    font-weight: 500;
    font-size: 15px;
    fill: var(--paper);
    letter-spacing: 0.3px;
  }
  .author-name {
    font-family: "Roboto", Arial, sans-serif;
    font-weight: 400;
    font-size: 31px;
    fill: var(--paper);
  }
</style>
</head>
<body>
  <div class="book-cover">
    <svg viewBox="0 0 475 735" xmlns="http://www.w3.org/2000/svg">
      <defs>
        <linearGradient id="alarmSky" x1="0" y1="0" x2="0" y2="1">
          <stop offset="0" stop-color="var(--alarm-red)"/>
          <stop offset="0.25" stop-color="var(--deep-red)"/>
          <stop offset="0.5" stop-color="var(--night)"/>
          <stop offset="1" stop-color="var(--night)"/>
        </linearGradient>
        <linearGradient id="capitolTones" x1="0" y1="0" x2="0" y2="1">
          <stop offset="0" stop-color="var(--smoke)" stop-opacity="0"/>
          <stop offset="0.3" stop-color="var(--smoke)" stop-opacity="0.7"/>
          <stop offset="0.6" stop-color="var(--stone)" stop-opacity="0.85"/>
          <stop offset="0.85" stop-color="var(--smoke)" stop-opacity="0.95"/>
          <stop offset="1" stop-color="#1c1d1f"/>
        </linearGradient>
      </defs>

      <rect class="cover-backdrop" x="0" y="0" width="475" height="735" fill="url(#alarmSky)"/>

      <rect class="capitol-photo" x="0" y="360" width="475" height="375" fill="url(#capitolTones)"
            role="img" aria-label="Greyscale photograph of the Capitol dome under a stormy sky"/>

      <text class="title-line" x="18" y="225" font-size="176" textLength="439" lengthAdjust="spacingAndGlyphs">FINAL</text>
      <text class="title-line" x="18" y="337" font-size="140" textLength="439" lengthAdjust="spacingAndGlyphs">HOUR</text>
      <text class="title-line title-line--accent" x="18" y="410" font-size="84" textLength="439" lengthAdjust="spacingAndGlyphs">TO RESCUE</text>
      <text class="title-line" x="18" y="527" font-size="150" textLength="439" lengthAdjust="spacingAndGlyphs">FREE</text>
      <text class="title-line" x="18" y="604" font-size="92" textLength="439" lengthAdjust="spacingAndGlyphs">REPUBLIC</text>

      <text class="subtitle" x="20" y="630">The Single Path to Halt the 2022 Partisan Takeover</text>
      <text class="subtitle" x="20" y="650">&amp; Renew Our Homeland</text>

      <line class="author-rule" x1="0" y1="665" x2="475" y2="665" stroke="var(--rule-red)" stroke-width="3"/>
      <text class="author-name" x="22" y="700">Corwin Hale Ashbury</text>
      <line class="author-rule" x1="0" y1="708" x2="475" y2="708" stroke="var(--rule-red)" stroke-width="3"/>
    </svg>
  </div>
</body>
</html>
```